6 - 8 'Holistic' Instagram Graphics

Hi there!
We are looking to build up a library of Graphic Templates to use as Instagram & Facebook posts for our Holistic Medi Spa (& 3 other companies eventually)
This competition is for a sample of 6 - 8 designs. For the winner(s), we will make an agreement for a batch order (Looking for 200+ designs in total), and will be looking to make a long term arrangement.
Please find a full job description in the attached Word Document.
Any questions, don't hesitate to ask.
Thanks!
Medical Spa

```html
<!DOCTYPE html>
<html lang="en">
<head>
<meta charset="utf-8">
<title>Holistic Spa Post Set</title>
<link href="https://fonts.googleapis.com/css2?family=Montserrat:wght@300;400;500;700;800&display=swap" rel="stylesheet">
<style>
:root{
  --blue:#36a7dc;
  --blue-deep:#2f93d2;
  --blue-light:#c6e8f6;
  --blue-pale:#e7f5fb;
  --ink:#0d0d0d;
  --author:#1b3d55;
  --white:#ffffff;
}
*{margin:0;padding:0;box-sizing:border-box}
html,body{width:1200px;height:753px;overflow:hidden;background:var(--white)}
body{position:relative;font-family:'Montserrat',sans-serif;color:var(--ink)}
.post{position:absolute;width:298px;height:298px;overflow:hidden;background:var(--white)}
.post svg.art{position:absolute;inset:0;width:298px;height:298px}
.post-quote{left:50px;top:46px}
.post-skincare{left:443px;top:46px}
.post-routine{left:848px;top:46px}
.post-ems{left:50px;top:404px}
.post-review{left:443px;top:404px}
.post-offer{left:848px;top:404px}
.copy{position:absolute;line-height:1;white-space:nowrap}
.quote-text{left:0;width:310px;top:50px;text-align:center;font-weight:800;font-size:29px;line-height:30px}
.quote-author{left:0;width:298px;top:172px;text-align:center;font-size:9.5px;font-weight:400;color:#333}
.skincare-title{left:36px;top:232px;font-size:33px;font-weight:800;letter-spacing:-.3px}
.skincare-sub{left:37px;top:270px;font-size:13.5px;font-weight:300}
.routine-text{left:0;width:298px;top:121px;text-align:center;font-size:20px;line-height:22px;font-weight:300}
.routine-text strong{font-weight:800}
.ems-text{left:20px;top:208px;font-size:19px;line-height:20px;font-weight:500}
.ems-text strong{font-weight:800}
.review-text{left:0;width:298px;top:188px;text-align:center;font-size:12.6px;line-height:16px;font-weight:500}
.review-mark{position:absolute;font-weight:800;font-size:30px;line-height:1}
.mark-open{left:50px;top:172px}
.mark-close{left:262px;top:220px}
.review-author{left:0;width:300px;top:258px;text-align:center;font-size:16px;font-weight:300;color:var(--author)}
.offer-text{left:0;width:298px;top:212px;text-align:center;font-size:17.5px;line-height:17.5px;font-weight:500}
.offer-text strong{font-weight:800}
</style>
</head>
<body>

<section class="post post-quote">
  <svg class="art" viewBox="0 0 298 298">
    <path fill="var(--blue)" d="M226,0 H298 V134 C262,142 232,132 236,100 C240,60 220,30 226,0 Z"/>
    <path fill="var(--blue-deep)" d="M0,96 C70,88 125,110 110,170 C100,220 84,260 84,298 H0 Z"/>
    <path fill="var(--blue-pale)" d="M110,298 C130,230 180,200 225,200 C265,200 290,230 298,250 V298 Z"/>
    <circle cx="116" cy="232" r="44" fill="var(--blue-light)"/>
  </svg>
  <p class="copy quote-text">A healthy<br>outside<br>starts from the<br>inside.</p>
  <p class="copy quote-author">Martin Hale</p>
</section>

<section class="post post-skincare">
  <svg class="art" viewBox="0 0 298 298">
    <defs>
      <linearGradient id="skinPhoto" x1="0" y1="0" x2="1" y2="1">
        <stop offset="0" stop-color="#bfc3d2"/>
        <stop offset=".45" stop-color="#e2c8bb"/>
        <stop offset=".7" stop-color="#d9b6a6"/>
        <stop offset="1" stop-color="#cfd2de"/>
      </linearGradient>
    </defs>
    <path role="img" aria-label="Portrait photo of a woman touching her jaw against a soft grey backdrop" fill="url(#skinPhoto)" d="M110,0 H298 V282 C250,286 210,275 175,285 C120,300 70,280 45,230 C25,180 30,120 60,95 C90,70 105,40 110,0 Z"/>
    <path fill="var(--blue)" d="M0,0 H132 C138,45 120,70 95,62 C70,55 45,70 20,60 C8,55 0,48 0,40 Z"/>
    <path fill="var(--blue-pale)" d="M0,205 C50,195 85,230 95,298 H0 Z"/>
  </svg>
  <h2 class="copy skincare-title">Skincare</h2>
  <p class="copy skincare-sub">for your soul</p>
</section>

<section class="post post-routine">
  <svg class="art" viewBox="0 0 298 298">
    <defs>
      <linearGradient id="routinePhoto" x1="0" y1="0" x2="1" y2="0">
        <stop offset="0" stop-color="#e4e6ee"/>
        <stop offset=".55" stop-color="#ebe2df"/>
        <stop offset=".8" stop-color="#e3cfc8"/>
        <stop offset="1" stop-color="#c9c2c2"/>
      </linearGradient>
    </defs>
    <rect role="img" aria-label="Photo of a woman in profile gently touching her face" width="298" height="298" fill="url(#routinePhoto)"/>
    <path fill="var(--blue-light)" opacity=".85" d="M0,0 H160 C160,60 120,90 90,110 C60,130 40,180 0,180 Z"/>
    <path fill="var(--blue)" d="M298,208 C250,250 215,240 180,205 C140,170 100,210 102,298 H298 Z"/>
  </svg>
  <p class="copy routine-text">When did you last<br>consider your<br><strong>skincare routine?</strong></p>
</section>

<section class="post post-ems">
  <svg class="art" viewBox="0 0 298 298">
    <defs>
      <linearGradient id="emsPhoto" x1="0" y1="0" x2="0" y2="1">
        <stop offset="0" stop-color="#d3d9e0"/>
        <stop offset=".55" stop-color="#e6e9ec"/>
        <stop offset="1" stop-color="#ffffff"/>
      </linearGradient>
    </defs>
    <rect role="img" aria-label="Photo of a woman in an EMS training suit squatting on a balance ball in a bright gym" width="220" height="220" fill="url(#emsPhoto)"/>
    <path fill="var(--blue-deep)" d="M155,0 H298 V78 C260,90 250,125 210,118 C170,110 155,50 155,0 Z"/>
    <circle cx="238" cy="236" r="62" fill="var(--blue-light)"/>
  </svg>
  <p class="copy ems-text"><strong>EMS Body</strong><br>Sculpting is equivalent to<br><strong>16 weeks HIT Training</strong></p>
</section>

<section class="post post-review">
  <svg class="art" viewBox="0 0 298 298">
    <defs>
      <linearGradient id="reviewPhoto" x1="0" y1="0" x2="1" y2="0">
        <stop offset="0" stop-color="#dcc3b3"/>
        <stop offset=".4" stop-color="#ecd8c6"/>
        <stop offset=".75" stop-color="#ece6df"/>
        <stop offset="1" stop-color="#f2f2f2"/>
      </linearGradient>
    </defs>
    <rect role="img" aria-label="Photo of a young girl having her ear pierced by a gloved specialist" width="298" height="210" fill="url(#reviewPhoto)"/>
    <path fill="var(--blue-light)" d="M135,0 H298 V150 C250,145 240,90 200,60 C165,35 140,20 135,0 Z"/>
    <path fill="var(--blue)" d="M0,165 C40,180 70,155 110,157 C170,160 205,200 205,298 H0 Z"/>
  </svg>
  <span class="review-mark mark-open">“</span>
  <p class="copy review-text">I recently went to have<br>my 4 month old daughter's ears<br>peirced, and they were prompt<br>and professional. Excellent service!</p>
  <span class="review-mark mark-close">”</span>
  <p class="copy review-author">Jamie Cole</p>
</section>

<section class="post post-offer">
  <svg class="art" viewBox="0 0 298 298">
    <defs>
      <linearGradient id="offerPhoto" x1="0" y1="0" x2="1" y2="1">
        <stop offset="0" stop-color="#cfd3cf"/>
        <stop offset=".4" stop-color="#f0e4dc"/>
        <stop offset=".7" stop-color="#cfe3ec"/>
        <stop offset="1" stop-color="#8fc3dc"/>
      </linearGradient>
    </defs>
    <path fill="var(--blue)" d="M0,86 C45,78 65,110 60,160 C56,210 80,250 76,298 H0 Z"/>
    <path role="img" aria-label="Photo of two smiling women in towel turbans wearing under-eye patches" fill="url(#offerPhoto)" d="M37,0 H298 V128 C265,140 255,165 240,185 C220,205 170,206 130,182 C90,160 60,135 52,100 C45,70 40,35 37,0 Z"/>
  </svg>
  <p class="copy offer-text"><strong>FREE</strong><br>treatment<br>when you share post<br>with a friend</p>
</section>

</body>
</html>
```